Lumora Vita Healthcare Practitioner Multivitamin Detailing Brochure

We need a healthcare practitioner detailing brochure for a company based in Pretoria South Africa. The brochure is used to educate healthcare practitioners and persuade them to prescribe Lumora Vita Multivitamin in their daily practice. Find attached all the necessary text required in the brochure. We would like a 4 paged A4 sized brochure (i.e. A3 folded). We would like to see designs that use the same colour orange to match the supplement bottle and our funky modern brand look. I have attached our supplement design, content etc. The final design should communicate professionalism, confidence and encourage healthcare practitioners to prescribe the product.
Look and feel
Each slider illustrates characteristics of the customer's brand and the style your logo design should communicate.

```html
<!DOCTYPE html>
<html lang="en">
<head>
<meta charset="utf-8">
<title>Lumora Vita – Considerations for Supplements</title>
<link href="https://fonts.googleapis.com/css2?family=Montserrat:wght@700;800&family=Source+Sans+3:wght@400;700&display=swap" rel="stylesheet">
<style>
  :root {
    --brand-orange: #f47b20;
    --paper: #ffffff;
    --mist: #e6e7e9;
    --card: #fdfbef;
    --ink: #2b2b2b;
    --heading-ink: #222222;
    --leaf-green: #5f9a36;
    --papaya: #f39a3a;
  }
  * { box-sizing: border-box; margin: 0; padding: 0; }
  html, body { width: 849px; height: 1200px; overflow: hidden; background: var(--paper); }
  .page {
    position: relative;
    width: 849px;
    height: 1200px;
    overflow: hidden;
    background: var(--paper);
    font-family: "Source Sans 3", "Helvetica Neue", Arial, sans-serif;
    color: var(--ink);
  }
  .backdrop { position: absolute; inset: 0; width: 849px; height: 1200px; }
  .page-title {
    position: absolute;
    top: 50px; left: 0; width: 100%;
    text-align: center;
    font-family: "Montserrat", Arial, sans-serif;
    font-weight: 800;
    font-size: 25px;
    letter-spacing: 0.3px;
    color: #fff;
  }
  .info-card {
    position: absolute;
    left: 23px;
    width: 800px;
    background: var(--card);
    box-shadow: 0 3px 8px rgba(0,0,0,0.22);
    padding: 14px 22px 0 22px;
  }
  .info-card h2 {
    font-family: "Source Sans 3", Arial, sans-serif;
    font-weight: 700;
    font-size: 23px;
    color: var(--heading-ink);
    margin-bottom: 8px;
  }
  .info-card p {
    font-size: 15.2px;
    line-height: 18.6px;
    letter-spacing: 0.15px;
    padding-right: 8px;
  }
  .card-active { top: 111px; height: 252px; }
  .card-network { top: 396px; height: 256px; }
  .card-genetic { top: 681px; height: 259px; }
  .produce-photo {
    position: absolute;
    left: 0; top: 940px; width: 490px; height: 260px;
    background: linear-gradient(90deg, var(--leaf-green) 0%, var(--leaf-green) 40%, var(--papaya) 100%);
  }
</style>
</head>
<body>
<div class="page">
  <svg class="backdrop" viewBox="0 0 849 1200" aria-hidden="true">
    <polygon points="0,0 849,0 849,1200 0,1200 0,905 849,30" fill="var(--brand-orange)"/>
    <polygon points="0,0 849,0 849,105 0,105" fill="var(--brand-orange)"/>
    <polygon points="0,105 849,105 849,300 300,880 0,880" fill="var(--paper)"/>
    <polygon points="0,40 90,40 0,150" fill="var(--mist)"/>
    <polygon points="0,930 330,1200 0,1200" fill="var(--mist)"/>
  </svg>

  <h1 class="page-title">CONSIDERATIONS FOR SUPPLEMENTS</h1>

  <section class="info-card card-active">
    <h2>ACTIVE VS INACTIVE</h2>
    <p>Most B vitamins found in supplements are supplied in their inactive form, requiring methylation by the liver to convert them into their active form which can be used by the body. This requires an enzyme called methylenetetrahydrofolate reductase (MTHFR). A large percentage of the population is affected by a mutation in the MTHFR gene which instructs the body to produce this enzyme. As much as 50% of the population may be affected. MTHFR mutations affect the bodies ability to metabolise unmethylated forms of B vitamins namely folate and B12. Lumora Vita multivitamin contains the active forms of both folate and vitamin B12 which are immediately bioavailable.</p>
  </section>

  <section class="info-card card-network">
    <h2>DYNAMIC INTERPLAY</h2>
    <p>Antioxidants engulf free radicals causing a change in molecular structure. This causes the antioxidant itself to become a free radical, although relatively weak and not likely to cause additional harm. Within the body there exists a dynamic interplay between five key antioxidants, often referred to as the network antioxidants. These are vitamin C, vitamin E, Co Q10, lipoic acid and glutathione. These network antioxidants work together to boost and strengthen the entire system, and when used together they enhance the activity of each other and help maintain antioxidant balance. Lumora Vita Multivitamin contains four of the five key network antioxidants.</p>
  </section>

  <section class="info-card card-genetic">
    <h2>GENETIC VARIATIONS AND NUTRITIONAL REGIMENS</h2>
    <p>Many genetic polymorphisms confer both advantage and risk, depending on the health outcome of interest. Understanding the physiologic and biochemical consequences of specific gene variants, required cofactor support and the mechanisms that confer disease protection or risk enables the rational design of dietary and nutritional approaches that can provide maximum patient benefit.<br>
    Genetic variation has an important influence on human nutritional requirements, and the introduction of genomics has both highlighted the complexity of the interaction between genes and diet and offered opportunities to provide optimal nutrition for individuals to ultimately reduce the risk of chronic diseases and increase health and well-being into old age.</p>
  </section>

  <div class="produce-photo" role="img" aria-label="Photo of fresh lettuce, a broccoli floret and a halved papaya"></div>
</div>
</body>
</html>
```